Glenvora pond linings website template

We need a template for our new website. Glenvora is currently marketed through www.sheetvale.com.au, and we are moving the pond/dam linings to a dedicated site www.glenvora.com.au

The site is essentially brochureware. The content (less landing page & photo gallery) is on the new site to give you a better idea of what we do. We are also on Facebook.com/glenvora

We are looking for a template/style which we can adapt to the different sections of the site as required. We also get a lot of phone/tablet visitors so an alternative mobile layout would be a bonus, but by no means required.

I am proficient in HTML/CSS & javascript so can code most designs thrown at me.

Any icons or interface fonts should be freely available web fonts where possible.

Target Market(s)

We are targeting both landscape professionals (design & construction) as well as the DIY market for ponds/wateragrdens.

Industry/Entity Type

Moving

Requirements
Must have
• We need a design (preferably layered PSD or AI) as basis for our overall site look and feel. Fonts/iconography/layout are where we are lacking. We can do the HTML/CSS/JS/PHP internally.
Nice to have
• A style guide either in file or separate would be nice.
Layers with effect (i.e.. :hover, CSS3 transition endpoints, etc)

```html
<!DOCTYPE html>
<html lang="en">
<head>
<meta charset="utf-8">
<title>Glenvora — Custom made liners</title>
<link rel="stylesheet" href="https://fonts.googleapis.com/css2?family=Roboto:wght@300;400;500&family=Roboto+Condensed:wght@400;700&family=Lobster&display=swap">
<style>
:root{
  --deep-green:#027449;
  --nav-green:#77a33a;
  --nav-green-dark:#5f8a2a;
  --box-green:#6d9c33;
  --lime:#c6d92e;
  --navy:#0a3a78;
  --text:#666;
  --white:#fff;
}
*{margin:0;padding:0;box-sizing:border-box}
html,body{width:1120px;height:1200px;overflow:hidden;background:var(--white)}
body{position:relative;font-family:"Roboto",Arial,sans-serif;color:var(--text)}
.abs{position:absolute}

.brand{left:168px;top:40px;display:flex;align-items:center;gap:12px}
.brand-square{width:34px;height:34px;background:var(--box-green)}
.brand-name{font-family:"Roboto",Arial,sans-serif;font-weight:400;font-size:38px;letter-spacing:3px;color:var(--deep-green)}

.phone{right:170px;top:20px;display:flex;align-items:center;gap:6px;font-size:26px;font-weight:300;color:var(--deep-green)}
.search{left:766px;top:70px;width:185px;height:30px;border:1px solid #e2e2e2;display:flex;align-items:center;justify-content:space-between;padding:0 8px;font-size:13px;color:#999}

.main-nav{left:0;top:119px;width:1120px;height:38px;background:linear-gradient(var(--nav-green),#6f9b33);border-bottom:2px solid var(--nav-green-dark)}
.main-nav ul{position:absolute;left:168px;top:0;display:flex;list-style:none;border-left:1px solid var(--nav-green-dark)}
.main-nav li{width:98px;height:38px;line-height:38px;text-align:center;font-size:11.5px;color:var(--white);border-right:1px solid var(--nav-green-dark)}
.main-nav li.active{background:var(--deep-green)}

.hero-band{left:0;top:157px;width:1120px;height:385px;background:var(--deep-green)}
.tagline{left:0;top:174px;width:1120px;text-align:center;font-family:"Lobster",cursive;font-size:28px;color:var(--lime)}

.slider{left:168px;top:234px;width:783px;height:396px;background:linear-gradient(180deg,#4e6a3c 0%,#3f6b33 30%,#5b7a4e 55%,#d98a33 70%,#f0a048 100%)}
.slider-shadow{left:210px;top:628px;width:700px;height:14px;border-radius:50%;box-shadow:0 8px 10px -4px rgba(0,0,0,.35)}
.dots{left:521px;top:600px;display:flex;gap:5px}
.dots span{width:12px;height:12px;border-radius:50%;background:var(--white)}
.dots span.on{background:var(--deep-green)}
.ribbons{left:0;top:0;width:1120px;height:700px;pointer-events:none}

.welcome{left:168px;top:665px;font-size:29px;color:var(--navy);font-weight:400}
.welcome .a{color:var(--deep-green);font-weight:300}
.welcome .b{color:var(--lime);font-weight:500}
.intro{left:168px;top:710px;width:790px;font-size:13.3px;line-height:19px;letter-spacing:.3px}
.btn-more{left:168px;top:753px;height:26px;padding:0 14px 0 8px;line-height:26px;background:var(--navy);color:var(--white);font-size:13px;letter-spacing:.6px}

.reasons-title{left:0;top:788px;width:1120px;text-align:center;font-family:"Lobster",cursive;font-size:38px;color:var(--deep-green)}
.rule{top:816px;height:1px;width:160px}
.rule.l{left:207px;background:linear-gradient(90deg,transparent,#555)}
.rule.r{left:753px;background:linear-gradient(90deg,#555,transparent)}

.reason{top:858px;width:130px}
.reason .tile{width:108px;height:108px;background:var(--box-green);display:flex;align-items:center;justify-content:center}
.reason p{margin-top:7px;margin-left:-2px;font-family:"Roboto Condensed",Arial,sans-serif;font-weight:700;font-size:13.5px;line-height:19px;color:var(--navy)}

.btn-contact{left:506px;top:1030px;width:108px;height:36px;line-height:36px;text-align:center;background:var(--navy);color:var(--white);font-family:"Roboto Condensed",Arial,sans-serif;font-weight:700;font-size:13.5px}

.site-footer{left:0;top:1120px;width:1120px;height:80px;background:var(--deep-green);color:var(--white)}
.legal{position:absolute;left:170px;top:31px;font-size:11.5px}
.legal a{color:var(--white)}
.social{position:absolute;left:850px;top:24px;display:flex;gap:5px}
.social span{width:30px;height:30px;border-radius:50%;background:var(--white)}
</style>
</head>
<body>

<header>
  <div class="abs brand"><span class="brand-square"></span><span class="brand-name">GLENVORA</span></div>
  <div class="abs phone">
    <svg width="25" height="25" viewBox="0 0 25 25"><rect width="25" height="25" rx="4" fill="#6d9c33"/><path d="M8 5c1 0 2 3 2 4s-1 1.5-1 2c1 2 3 4 5 5 .5 0 1-1 2-1s4 1 4 2-1 3-3 3C11 20 5 14 5 8c0-2 2-3 3-3z" fill="#fff"/></svg>
    1300 555 018
  </div>
  <div class="abs search"><span>Search</span>
    <svg width="12" height="12" viewBox="0 0 12 12"><circle cx="5" cy="5" r="3.5" fill="none" stroke="#0a3a78" stroke-width="1.8"/><path d="M7.5 7.5 11 11" stroke="#0a3a78" stroke-width="2"/></svg>
  </div>
</header>

<nav class="abs main-nav">
  <ul>
    <li class="active">HOME</li><li>ABOUT US</li><li>HAPPENINGS</li><li>GALLERY</li><li>LINER STYLES</li><li>PREPARATION</li><li>INSTALLATION</li><li>CONTACT US</li>
  </ul>
</nav>

<section>
  <div class="abs hero-band"></div>
  <div class="abs tagline">Custom made liners for ponds, pools &amp; watergardens</div>
  <div class="abs slider-shadow"></div>
  <div class="abs slider" role="img" aria-label="Project photo: lined pond with waterfall, ferns and a timber deck"></div>
  <div class="abs dots"><span></span><span></span><span class="on"></span><span></span><span></span></div>
  <svg class="abs ribbons" viewBox="0 0 1120 700">
    <polygon points="160,304 228,234 292,228 160,370" fill="#0a3a78"/>
    <text x="0" y="0" transform="translate(212,287) rotate(-45)" text-anchor="middle" fill="#fff" font-family="Roboto,Arial,sans-serif" font-size="14">OUR PROJECTS</text>
    <polygon points="828,638 960,496 960,560 888,638" fill="#6d9c33"/>
    <polygon points="951,506 960,496 951,496" fill="#3f6b1f"/>
    <text x="0" y="0" transform="translate(910,584) rotate(-45)" text-anchor="middle" fill="#fff" font-family="Roboto,Arial,sans-serif" font-size="14">CONTACT US</text>
  </svg>
</section>

<main>
  <h1 class="abs welcome">Welcome to <span class="a">GLEN</span><span class="b">VORA</span></h1>
  <p class="abs intro">Glenvora has been manufactured, marketed and installed throughout Australia and the Pacific Rim since the early 1980’s for a variety of domestic and commercial applications.</p>
  <div class="abs btn-more">Know More</div>

  <div class="abs rule l"></div>
  <h2 class="abs reasons-title">5 Reasons to choose us</h2>
  <div class="abs rule r"></div>

  <div class="abs reason" style="left:210px">
    <div class="tile"><svg width="50" height="50" viewBox="0 0 50 50"><circle cx="25" cy="25" r="25" fill="#fff"/><circle cx="25" cy="25" r="17" fill="#6d9c33"/><circle cx="25" cy="25" r="13" fill="#fff"/><path d="M25 15v11h8" fill="none" stroke="#6d9c33" stroke-width="4"/></svg></div>
    <p>EASIER &amp; QUICKER<br>INSTALLATION</p>
  </div>
  <div class="abs reason" style="left:359px">
    <div class="tile"><svg width="52" height="52" viewBox="0 0 52 52"><polygon fill="#fff" points="26,1 31,7 38,4 40,12 48,13 45,20 51,26 45,32 48,39 40,40 38,48 31,45 26,51 21,45 14,48 12,40 4,39 7,32 1,26 7,20 4,13 12,12 14,4 21,7"/><text x="26" y="33" text-anchor="middle" font-family="Roboto Condensed,Arial,sans-serif" font-weight="700" font-size="19" fill="#6d9c33">20</text></svg></div>
    <p>20 YEARS<br>GUARANTEE</p>
  </div>
  <div class="abs reason" style="left:507px">
    <div class="tile"><svg width="50" height="50" viewBox="0 0 50 50"><circle cx="25" cy="25" r="14" fill="none" stroke="#fff" stroke-width="7"/><g fill="#fff"><rect x="21" y="0" width="8" height="13" rx="3"/><rect x="21" y="37" width="8" height="13" rx="3"/><rect x="0" y="21" width="13" height="8" rx="3"/><rect x="37" y="21" width="13" height="8" rx="3"/></g></svg></div>
    <p>FLEXIBLE TO ALL<br>CONDITIONS</p>
  </div>
  <div class="abs reason" style="left:655px">
    <div class="tile"><svg width="50" height="50" viewBox="0 0 50 50"><rect width="50" height="50" rx="8" fill="#fff"/><path d="M25 10v30M10 25h30" stroke="#6d9c33" stroke-width="9"/></svg></div>
    <p>ANY SIZE<br>OR SHAPE</p>
  </div>
  <div class="abs reason" style="left:803px">
    <div class="tile"><svg width="50" height="50" viewBox="0 0 50 50"><circle cx="25" cy="25" r="25" fill="#fff"/><text x="25" y="38" text-anchor="middle" font-family="Roboto,Arial,sans-serif" font-weight="500" font-size="38" fill="#6d9c33">$</text></svg></div>
    <p>MOST<br>ECONOMICAL</p>
  </div>

  <div class="abs btn-contact">CONTACT US</div>
</main>

<footer class="abs site-footer">
  <p class="legal">© 2003 Glenvora. All rights reserved. <a href="#">Privacy Policy</a> &nbsp;| &nbsp;<a href="#">Terms of Use</a></p>
  <div class="social" aria-label="Social links"><span></span><span></span><span></span></div>
</footer>

</body>
</html>
```